Laser Tattoo Removal Business Cards

We are looking for a professional business card design for a laser tattoo removal business. Ideally looking for a black business card design. The name of the business is Brightmoor Ink Erasure. We place our cards at local tattoo shops so we ideally are looking for something trendy/edgy to draw both male and female clientele in.

Target Market(s)

Male/Female ages 18-60

Contact Information for Business Card

black background ideally.. hoping to stay within greys, whites and black

Font styles to use
Serif
Sans Serif

Colors
121212
a9a9a9
5c5c5c
f5f5f5
ffffff
7f7f7f
606060
848484
9d9d9d

Requirements
Must have
• Employee Info:
• Melissa Danforth
• Chief Executive Offer
• m: 919.555.0143
• w: 919.555.0187
• f: 919.555.0162
• mdanforth@brightmoorinkerasure.com
• Address:
• 4518 Pell Ridge Dr, Suite 210
• Raleigh, NC 27699
• Website:
• www.brightmoorinkerasure.com
Nice to have
• Myabe business name on back or logo on back and employee info on the front

```html
<!DOCTYPE html>
<html lang="en">
<head>
<meta charset="utf-8">
<title>Brightmoor Ink Erasure — Business Card</title>
<link rel="stylesheet" href="https://fonts.googleapis.com/css2?family=Lato:wght@400;700;900&family=Arimo:wght@400&display=swap">
<style>
  :root{
    --ink:#121212;
    --paper:#d9d9d9;
    --paper-light:#f5f5f5;
    --white:#ffffff;
    --grey-dark:#5c5c5c;
    --grey-mid:#7f7f7f;
    --grey-soft:#a9a9a9;
    --backdrop:#3a3a3a;
  }
  *{margin:0;padding:0;box-sizing:border-box}
  html,body{width:1200px;height:896px;overflow:hidden}
  body{
    background:var(--backdrop);
    font-family:"Arimo",Arial,sans-serif;
    position:relative;
  }
  .card{
    position:absolute;
    left:250px;
    width:700px;
    height:400px;
    box-shadow:0 8px 24px rgba(0,0,0,.35);
  }
  .card--front{top:32px;background:var(--paper);color:var(--ink)}
  .card--back{top:464px;background:var(--ink);color:var(--white)}

  /* front */
  .employee{position:absolute;left:56px;top:70px}
  .employee__name{
    font-family:"Lato",sans-serif;font-weight:900;
    font-size:27px;letter-spacing:-.3px;text-transform:uppercase;line-height:1;
  }
  .employee__title{font-size:21px;margin-top:4px;color:#222}
  .contact-list{list-style:none;margin-top:8px}
  .contact-list li{display:flex;align-items:center;gap:10px;font-size:21px;line-height:27px}
  .contact-list svg{width:16px;height:18px;flex:none}
  .divider{position:absolute;height:1px;background:var(--grey-dark)}
  .card--front .divider{left:300px;right:48px;top:250px}
  .brand{
    font-family:"Lato",sans-serif;font-weight:700;
    text-transform:uppercase;letter-spacing:4px;line-height:1.12;text-align:center;
  }
  .card--front .brand{position:absolute;right:56px;top:96px;font-size:34px}
  .address{
    position:absolute;right:56px;bottom:60px;text-align:right;
    font-size:22px;line-height:28px;
  }

  /* back */
  .card--back .brand{position:absolute;left:0;right:0;top:96px;font-size:36px;color:var(--white)}
  .card--back .divider{left:150px;right:150px;top:220px;background:var(--grey-soft)}
  .web{
    position:absolute;left:170px;top:240px;
    font-size:21px;line-height:28px;color:var(--paper-light);
  }
</style>
</head>
<body>

<section class="card card--front" aria-label="Business card front">
  <div class="employee">
    <h1 class="employee__name">Melissa Danforth</h1>
    <p class="employee__title">Chief Executive Officer</p>
    <ul class="contact-list">
      <li>
        <svg viewBox="0 0 16 18" aria-label="mobile"><rect x="3.5" y="1" width="9" height="16" rx="1.5" fill="none" stroke="currentColor" stroke-width="1.6"/><line x1="6.5" y1="14.5" x2="9.5" y2="14.5" stroke="currentColor" stroke-width="1.4"/></svg>
        919.555.0143
      </li>
      <li>
        <svg viewBox="0 0 16 18" aria-label="phone"><path d="M4 2l3 3-1.6 2c.9 2 2.3 3.6 4.4 4.6L11.8 10l3 3-1.6 2.2C7.8 15 2.6 9.7 2 4.2z" fill="currentColor"/></svg>
        919.555.0187
      </li>
      <li>
        <svg viewBox="0 0 16 18" aria-label="fax"><rect x="4" y="2" width="8" height="5" fill="none" stroke="currentColor" stroke-width="1.4"/><rect x="1" y="7" width="14" height="7" rx="1" fill="currentColor"/><rect x="4" y="12" width="8" height="4" fill="currentColor" stroke="var(--paper)" stroke-width="1"/></svg>
        919.555.0162
      </li>
    </ul>
  </div>

  <div class="brand">Brightmoor<br>Ink Erasure</div>
  <div class="divider"></div>

  <address class="address" style="font-style:normal">
    4518 Pell Ridge Dr, Suite 210<br>
    Raleigh, NC 27699
  </address>
</section>

<section class="card card--back" aria-label="Business card back">
  <div class="brand">Brightmoor<br>Ink Erasure</div>
  <div class="divider"></div>
  <p class="web">
    mdanforth@brightmoorinkerasure.com<br>
    www.brightmoorinkerasure.com
  </p>
</section>

</body>
</html>
```